Jotle - sticky notes for Orchard OS landing page single page html + css

Is landing page for a new Orchard OS app, I need just one single page explaing some features.

I will attach some materials to get insiprations.

Should be used the latest model of devices and some nice features
you can try the app here http://qv.example/f/K8R2

Jotle is a simple note taking app for Orchard OS

Features:
- SkyVault Sync on differnt Orchard
- Private notes
- PressKey Support on Orchard to quick unlock
- Custom Colors
- Rich Text editing
- Glide Strip support
- Autolock private notes after user activity

some text should be present as spot
Updates

We have a new icon: http://qv.example/i/pm47

Project Deadline Extended
Reason: Delayed to have more time to develope ideas

Target Market(s)

US

Industry/Entity Type

Software

Coding

Coded - Design and coding required

Number of Pages Required

1 page

Font styles to use
Sans Serif

Colors
fbed22

Requirements
Must have
• Fast load and adaptable to verious devices
• some menu that point down to the features sections
• - link to Desk App Depot with badge
• - Form to subscribe a newsletter
• - Use some claim text
• - Avenir font
• some screenshot of the prduct
Nice to have
• some animations but not to much
• references:
• http://quillhourapp.example
• https://marovinapp.example
• http://www.hueforge.example/mac/
• https://crankworks.example/clipmule/
• https://crankworks.example/chirpling/mac/
• http://www.otter-scribe.example
Should not have
• slow load

```html
<!DOCTYPE html>
<html lang="en">
<head>
<meta charset="utf-8">
<title>Jotle – simple note taking for Orchard OS</title>
<link rel="stylesheet" href="https://fonts.googleapis.com/css2?family=Mulish:wght@400;600;700&family=Open+Sans:wght@400;600;700&display=swap">
<style>
:root{
  --brand:#fbed22;
  --brand-deep:#f6c400;
  --ink:#1d1d1d;
  --text:#444;
  --muted:#777;
  --rule:#e2e2e2;
  --paper:#ffffff;
  --sky:#9ff3f6;
  --leaf:#cdee8a;
}
*{box-sizing:border-box;margin:0;padding:0}
html,body{width:1200px;height:2857px;overflow:hidden;background:var(--paper)}
body{position:relative;font-family:"Open Sans",Arial,sans-serif;color:var(--text)}
.abs{position:absolute}
.center{left:0;width:1200px;text-align:center}
h1,h2,h3,.brand-name{font-family:"Mulish","Nunito Sans",sans-serif;color:var(--ink)}
.divider{position:absolute;left:99px;width:1002px;height:1px;background:var(--rule)}

/* header */
.demo-btn{left:822px;top:40px;width:212px;height:42px;border:1.5px solid #333;border-radius:21px;font:700 12px "Open Sans",sans-serif;color:var(--ink);display:flex;align-items:center;justify-content:center;letter-spacing:.3px;white-space:nowrap}
.menu-btn{left:1055px;top:38px;width:46px;height:46px;border:1.5px solid #333;border-radius:50%}

/* brand mark */
.brand{display:flex;align-items:center;justify-content:center;gap:18px}
.brand-dot{border-radius:50%;background:var(--brand)}
.brand-name{font-weight:600;color:var(--ink)}

.hero-title{top:268px;font-size:38px;font-weight:700;white-space:nowrap}
.hero-lead{top:330px;left:250px;width:700px;text-align:center;font-size:16.5px;line-height:27px;color:var(--text)}
.subscribe{left:347px;top:411px;width:506px;height:44px;display:flex}
.subscribe .field{flex:1;border:1px solid #bbb;border-right:none;font-size:13px;color:#888;padding-left:18px;display:flex;align-items:center}
.subscribe .go{width:137px;background:var(--brand);border:1px solid #e4d200;font:700 15px "Open Sans",sans-serif;color:var(--ink);display:flex;align-items:center;justify-content:center;letter-spacing:.4px}
.store-badge{left:518px;top:482px;width:162px;height:46px;background:#111;border-radius:6px}

.section-title{font-size:29px;font-weight:700}
.welcome-copy{left:250px;top:710px;width:700px;text-align:center;font-size:11.5px;line-height:20px;color:var(--muted)}
.devices{left:267px;top:823px;width:613px;height:312px}

/* features */
.feature{position:absolute;width:330px;text-align:center}
.feature svg{display:block;margin:0 auto 18px}
.feature h3{font-size:18px;font-weight:700;margin-bottom:10px;white-space:nowrap}
.feature p{font-size:11.5px;line-height:24px;color:var(--text)}
.more-btn{left:511px;top:1760px;width:179px;height:44px;border:1.5px solid #333;border-radius:22px;font:700 13px "Open Sans",sans-serif;color:var(--ink);display:flex;align-items:center;justify-content:center}

/* devices section */
.phone-shot{left:91px;top:1934px;width:229px;height:444px;border-radius:38px}
.sync-diagram{left:590px;top:2019px;width:328px;height:149px;border-radius:6px}
.variant{position:absolute;top:2297px;display:flex;gap:18px}
.swatch{width:63px;height:57px;border:1px solid #888}
.variant h3{font-size:15px;font-weight:700;margin-bottom:6px}
.variant p{font-size:11.5px;line-height:22px;color:var(--muted);width:170px}

/* footer */
.social{left:507px;top:2636px;width:183px;display:flex;justify-content:space-between}
.social span{width:18px;height:18px;border-radius:50%;background:#222}
.footer-links{top:2684px;font-size:12.5px;color:var(--ink)}
.footer-links span{margin:0 8px;color:#555}
.copyright{top:2723px;font-size:12.5px;color:var(--ink)}
.footer-note{left:200px;top:2764px;width:800px;text-align:center;font-size:11px;line-height:23px;color:var(--ink)}
</style>
</head>
<body>

<header>
  <div class="abs demo-btn">TRY THE ORCHARD DEMO</div>
  <div class="abs menu-btn">
    <svg width="46" height="46" viewBox="0 0 46 46"><g stroke="#222" stroke-width="2.4"><line x1="16" y1="17" x2="30" y2="17"/><line x1="16" y1="23" x2="30" y2="23"/><line x1="16" y1="29" x2="30" y2="29"/></g></svg>
  </div>
  <div class="abs center brand" style="top:112px">
    <span class="brand-dot" style="width:70px;height:70px"></span>
    <span class="brand-name" style="font-size:64px">Jotle</span>
  </div>
</header>

<section class="hero">
  <h1 class="abs center hero-title">Jotle is a simple note taking app for Orchard OS</h1>
  <p class="abs hero-lead">At vero eos et accusamus et iusto odio dignissimos ducimus qui blanditiis praesentium voluptatum deleniti atque corrupti quos dolores et quas molestias excep</p>
  <form class="abs subscribe">
    <div class="field">Email Address</div>
    <div class="go">SUBSCRIBE</div>
  </form>
  <div class="abs store-badge" role="img" aria-label="Desk App Depot download badge"></div>
</section>

<div class="divider" style="top:590px"></div>

<section class="welcome">
  <h2 class="abs center section-title" style="top:650px">Welcome to Jotle</h2>
  <p class="abs welcome-copy">Nemo enim ipsam voluptatem quia voluptas sit aspernatur aut odit aut fugit, sed quia consequuntur magni dolores eos qui ratione voluptatem sequi nesciunt. Neque porro quisquam est, qui dolorem ipsum quia dolor sit amet, consectetur, adipisci velit, sed quia non numquam eius modi tempora incidunt ut labore et dolore magnam aliquam</p>
  <div class="abs devices" role="img" aria-label="Jotle running on a laptop, tablet and phone, with coloured notes on the desktop" style="background:linear-gradient(90deg,#f7d800 0%,#f5e04a 30%,#2b3f6e 45%,#3a4f86 75%,#d8d8d8 100%);border-radius:8px"></div>
</section>

<div class="divider" style="top:1213px"></div>

<section class="features" id="features">
  <h2 class="abs center section-title" style="top:1262px">Our Features</h2>

  <div class="feature" style="left:77px;top:1343px">
    <svg width="72" height="68" viewBox="0 0 72 68"><path d="M18 44a12 12 0 0 1 2-24 16 16 0 0 1 31 3 10 10 0 0 1 1 21z" fill="#f6c400"/><path d="M36 30v30M28 52l8 8 8-8" stroke="#f6c400" stroke-width="4" fill="none"/><path d="M36 30v20" stroke="#fff" stroke-width="3"/></svg>
    <h3>SkyVault Sync on differnt Orchard</h3>
    <p>Neque porro quisquam est, qui dolorem ipsum quia dolor sit amet consectetur adipisci velit ed</p>
  </div>
  <div class="feature" style="left:435px;top:1343px">
    <svg width="72" height="68" viewBox="0 0 72 68"><path d="M6 12h22l6 6h30v40H6z" fill="#f6c400"/><circle cx="52" cy="50" r="14" fill="#fff"/><rect x="44" y="48" width="16" height="12" rx="2" fill="#f6c400"/><path d="M47 48v-4a5 5 0 0 1 10 0v4" stroke="#f6c400" stroke-width="3" fill="none"/></svg>
    <h3>Private notes</h3>
    <p>Neque porro quisquam est, qui dolorem ipsum quia dolor sit amet consectetur adipisci velit ed</p>
  </div>
  <div class="feature" style="left:791px;top:1343px">
    <svg width="72" height="68" viewBox="0 0 72 68"><g fill="none" stroke="#f6c400" stroke-width="3"><path d="M20 30a16 16 0 0 1 32 0v14"/><path d="M26 32a10 10 0 0 1 20 0v20"/><path d="M32 34a4 4 0 0 1 8 0v26"/><path d="M20 36v12M14 26a22 22 0 0 1 44 0"/></g></svg>
    <h3>PressKey Support on Orchard</h3>
    <p>Neque porro quisquam est, qui dolorem ipsum quia dolor sit amet consectetur adipisci velit ed</p>
  </div>

  <div class="feature" style="left:77px;top:1547px">
    <svg width="72" height="72" viewBox="0 0 72 72"><path d="M44 10l18 18-8 4-14-14z" fill="#f6c400"/><path d="M40 24l8 8-28 28-10 4 4-10z" fill="#f6c400"/></svg>
    <h3>Custom Colors</h3>
    <p>Neque porro quisquam est, qui dolorem ipsum quia dolor sit amet consectetur adipisci velit ed</p>
  </div>
  <div class="feature" style="left:435px;top:1547px">
    <svg width="72" height="72" viewBox="0 0 72 72"><rect x="12" y="8" width="40" height="56" rx="4" fill="#f6c400"/><g stroke="#fff" stroke-width="3"><line x1="20" y1="22" x2="40" y2="22"/><line x1="20" y1="32" x2="36" y2="32"/><line x1="20" y1="42" x2="32" y2="42"/></g><path d="M58 16l6 6-24 24-8 2 2-8z" fill="#f6c400" stroke="#fff" stroke-width="2"/></svg>
    <h3>Rich Text editing</h3>
    <p>Neque porro quisquam est, qui dolorem ipsum quia dolor sit amet consectetur adipisci velit ed</p>
  </div>
  <div class="feature" style="left:791px;top:1547px">
    <svg width="72" height="72" viewBox="0 0 72 72"><circle cx="32" cy="30" r="22" fill="#f6c400"/><circle cx="32" cy="30" r="14" fill="none" stroke="#fff" stroke-width="3"/><path d="M40 44h14a6 6 0 0 1 6 6v14H40z" fill="#f6c400" stroke="#fff" stroke-width="2"/></svg>
    <h3>Glide Strip support</h3>
    <p>Neque porro quisquam est, qui dolorem ipsum quia dolor sit amet consectetur adipisci velit ed</p>
  </div>

  <div class="abs more-btn">VIEW MORE &gt;&gt;</div>
</section>

<div class="divider" style="top:1857px"></div>

<section class="everywhere">
  <div class="abs phone-shot" role="img" aria-label="Jotle welcome screen on a phone" style="background:linear-gradient(180deg,#f2f2f2 0%,#f2f2f2 12%,#ffe600 13%,#f6c400 85%,#f2f2f2 86%);border:2px solid #ccc"></div>
  <div class="abs center brand" style="left:590px;width:290px;top:1938px">
    <span class="brand-dot" style="width:44px;height:44px"></span>
    <span class="brand-name" style="font-size:40px">Jotle</span>
  </div>
  <div class="abs sync-diagram" role="img" aria-label="Illustration of a note syncing from phone to tablet to laptop with dotted arrows" style="background:linear-gradient(135deg,#f4f4f4 0%,#fbf3a0 50%,#e6e6e6 100%)"></div>
  <h2 class="abs center" style="left:381px;width:780px;top:2220px;font-size:26px;font-weight:700">The same Jotle on all your devices</h2>

  <div class="variant" style="left:381px">
    <div class="swatch" style="background:#fff200"></div>
    <div><h3>Universal Jotle</h3><p>Share and edit onPocketOS, and Orchard OS, and PaneOS</p></div>
  </div>
  <div class="variant" style="left:638px">
    <div class="swatch" style="background:var(--sky)"></div>
    <div><h3>Desktop Jotle</h3><p>Read on PocketOS, and Edit Orchard OS</p></div>
  </div>
  <div class="variant" style="left:876px">
    <div class="swatch" style="background:var(--leaf)"></div>
    <div><h3>Private Jotle</h3><p>Needs to use your password to access the content</p></div>
  </div>
</section>

<div class="divider" style="top:2463px"></div>

<footer>
  <div class="abs center brand" style="top:2530px">
    <span class="brand-dot" style="width:48px;height:48px"></span>
    <span class="brand-name" style="font-size:44px">Jotle</span>
  </div>
  <div class="abs social" aria-label="Social links"><span></span><span></span><span></span><span></span><span></span></div>
  <p class="abs center footer-links">Orchard App<span>|</span>PocketOS App<span>|</span>Sync<span>|</span>Publish<span>|</span>Support<span>|</span>Jobs<span>|</span>Newsletter<span>|</span>Press<span>|</span>Login</p>
  <p class="abs center copyright">Copyrights © 2017, Jotle. All rights reserved.</p>
  <p class="abs footer-note">At vero eos et accusamus et iusto odio dignissimos ducimus qui blanditiis praesentium voluptatum deleniti atque corrupti quos dolores et quas molestias excepturi sint occaecati cupiditate non provident, similique sunt in culpa qui officia deserunt mollitia ani est laborum</p>
</footer>

</body>
</html>
```